Business Card and Stationery for Bellwick Home Services
Bellwick Home Services
Professional
R. Owen Tallis
President/CEO
4187 Marrow Creek Lane,
Suite K
Baton Rouge LA 70342
rowentallis@bellwickhomeservices.biz
www.bellwickhomeservice.biz
Commercial License # 53419 Residential LIcense # 21398
The color formula for the orange is:
C=0 M=74 Y=100 K=0
We take care of all of your home needs.
Plumbing, Heating and AIr, Electrical, Remodeling, Roofing, New Construction, Insurance Damage Repairs, Fire Restoration, if its in you home, we can service it or take care of it for you!!!
THESE ARE JUST IDEAS, want to use the back for information, etc.......maybe a light watermark on the back, using part of the logo, showing under the lettering. Would like the back to be the orange color

```html
<!DOCTYPE html>
<html lang="en">
<head>
<meta charset="utf-8">
<title>Bellwick Home Services – Business Card</title>
<link rel="stylesheet" href="https://fonts.googleapis.com/css2?family=Open+Sans:wght@400;600;700;800&display=swap">
<style>
  :root {
    --orange: #f15a22;
    --ink: #4a4a4a;
    --muted: #7a7a7a;
    --paper: #ffffff;
    --stage: #ecebe8;
    --watermark: rgba(255,255,255,.10);
  }
  * { box-sizing: border-box; margin: 0; padding: 0; }
  html, body { width: 1200px; height: 629px; overflow: hidden; }
  body {
    background: var(--stage);
    font-family: "Open Sans", Arial, sans-serif;
    display: flex; align-items: center; justify-content: center; gap: 48px;
  }
  .card {
    width: 525px; height: 300px; position: relative; overflow: hidden;
    box-shadow: 0 6px 18px rgba(0,0,0,.15);
  }

  /* Back */
  .card-back { background: var(--orange); color: var(--paper); }
  .card-back .watermark {
    position: absolute; right: 60px; top: 30px; width: 200px; height: 200px;
    background: var(--watermark);
  }
  .card-back .back-text {
    position: absolute; left: 40px; right: 40px; top: 96px; z-index: 1;
  }
  .back-headline { font-size: 15px; font-weight: 700; margin-bottom: 10px; }
  .back-services { font-size: 11px; line-height: 1.6; font-weight: 400; }
  .back-license { font-size: 10.5px; margin-top: 12px; font-weight: 600; }

  /* Front */
  .card-front { background: var(--paper); }
  .brand { position: absolute; left: 38px; top: 36px; display: flex; align-items: center; gap: 14px; }
  .brand-square { width: 64px; height: 64px; background: var(--orange); border-radius: 6px; }
  .brand-name { font-size: 22px; font-weight: 800; color: var(--orange); line-height: 1.1; }
  .person { position: absolute; left: 38px; top: 140px; }
  .person-name { font-size: 15px; font-weight: 700; color: var(--orange); }
  .person-title { font-size: 11px; color: var(--muted); margin-bottom: 12px; }
  .person-address { font-size: 11px; line-height: 1.5; color: var(--ink); }
  .contacts { position: absolute; left: 270px; top: 120px; list-style: none; }
  .contacts li { display: flex; align-items: center; gap: 8px; font-size: 10.5px; color: var(--ink); margin-bottom: 7px; white-space: nowrap; }
  .contacts svg { width: 16px; height: 16px; flex: none; }
  .web-band {
    position: absolute; left: 0; right: 0; bottom: 0; height: 30px;
    background: var(--orange); color: var(--paper);
    font-size: 12px; font-weight: 600; letter-spacing: 2px;
    display: flex; align-items: center; justify-content: center;
  }
</style>
</head>
<body>

<section class="card card-back">
  <div class="watermark" aria-hidden="true"></div>
  <div class="back-text">
    <p class="back-headline">We take care of all of your home needs.</p>
    <p class="back-services">Plumbing, Heating and Air, Electrical, Remodeling, Roofing, New Construction, Insurance Damage Repairs, Fire Restoration, if it's in your home, we can service it or take care of it for you!!!</p>
    <p class="back-license">Commercial License # 53419 &nbsp;·&nbsp; Residential License # 21398</p>
  </div>
</section>

<section class="card card-front">
  <div class="brand">
    <div class="brand-square" aria-hidden="true"></div>
    <div class="brand-name">Bellwick<br>Home Services</div>
  </div>

  <div class="person">
    <p class="person-name">R. Owen Tallis</p>
    <p class="person-title">President/CEO</p>
    <p class="person-address">4187 Marrow Creek Lane,<br>Suite K<br>Baton Rouge LA 70342</p>
  </div>

  <ul class="contacts">
    <li><svg viewBox="0 0 16 16"><circle cx="8" cy="8" r="8" fill="#f15a22"/><path d="M5.5 4.5l1.5 1.5-.8 1a5 5 0 002.8 2.8l1-.8 1.5 1.5-1 1.2c-3 0-6.2-3.2-6.2-6.2z" fill="#fff"/></svg>225-555-0142</li>
    <li><svg viewBox="0 0 16 16"><circle cx="8" cy="8" r="8" fill="#f15a22"/><rect x="5.5" y="3.5" width="5" height="9" rx="1" fill="#fff"/></svg>225-555-0187</li>
    <li><svg viewBox="0 0 16 16"><circle cx="8" cy="8" r="8" fill="#f15a22"/><rect x="4.5" y="6" width="7" height="5" fill="#fff"/><rect x="5.5" y="4" width="5" height="2" fill="#fff"/></svg>225-555-0163</li>
    <li><svg viewBox="0 0 16 16"><circle cx="8" cy="8" r="8" fill="#f15a22"/><rect x="4" y="5" width="8" height="6" fill="#fff"/><path d="M4 5l4 3.5L12 5" stroke="#f15a22" fill="none"/></svg>rowentallis@bellwickhomeservices.biz</li>
    <li><svg viewBox="0 0 16 16"><circle cx="8" cy="8" r="8" fill="#f15a22"/><circle cx="8" cy="8" r="3.5" fill="#fff"/></svg>rowentallis</li>
  </ul>

  <div class="web-band">www.bellwickhomeservice.biz</div>
</section>

</body>
</html>
```